Stock Market Research Company Needs a new Design for our Podcast

We need a new logo and social media images for our podcast called Ledger Chat Podcast. We have a current design and logo but are looking to update the branding of the podcast. The podcast is highly interactive taking listener questions each week on individual stocks as well as stock portfolio building strategies.

Copy of Ledger Chat Podcast Thumbnail is our current branding.

Podcast Ad 2 Image attached for an idea of what we're looking for but using our specific colours.

Incorporate K from our current logo (attached)
Colours: Primary Color: (#1AA897), Secondary Color (#2E4151)
Clean/Modern style
Include Headshots of Hosts (images attached)

Target Market(s)

Podcast listeners and stock market investors

Industry/Entity Type

Investment

Logo Text

Title - Ledger Chat Podcast. Tagline - Stock Picks, Strategies & Tips For All Investors

Colors
33b8a4
86cfc6
00a990

Requirements
Must have
• Incorporate K from our current logo (attached)
Clean/Modern style

```html
<!DOCTYPE html>
<html lang="en">
<head>
<meta charset="utf-8">
<title>Ledger Chat Podcast</title>
<link rel="stylesheet" href="https://fonts.googleapis.com/css2?family=Bebas+Neue&family=Montserrat:wght@300;400&display=swap">
<style>
  :root {
    --ink: #000000;
    --teal: #639e93;
    --gold-band: #c9ac34;
    --gold-text: #d8c42c;
    --white: #ffffff;
    --footer: rgba(58, 58, 58, 0.9);
  }
  html, body {
    margin: 0;
    padding: 0;
    width: 1200px;
    height: 1197px;
    overflow: hidden;
    background: var(--ink);
  }
  .cover {
    position: relative;
    width: 1200px;
    height: 1197px;
    background: var(--ink);
    overflow: hidden;
    font-family: "Bebas Neue", "Oswald", sans-serif;
  }
  .title-block {
    position: absolute;
    left: 194px;
    top: 0;
    width: 813px;
    height: 236px;
    background: var(--teal);
  }
  .title {
    position: absolute;
    left: 0;
    right: 0;
    top: 30px;
    margin: 0;
    text-align: center;
    color: var(--white);
    font-size: 188px;
    line-height: 1;
    font-weight: 400;
    letter-spacing: 0;
    white-space: nowrap;
  }
  .format-badge {
    position: absolute;
    left: 409px;
    top: 207px;
    width: 383px;
    height: 61px;
    background: var(--gold-band);
    color: var(--ink);
    font-size: 56px;
    line-height: 63px;
    text-align: center;
    letter-spacing: 0.42em;
    text-indent: 0.42em;
  }
  .tagline {
    position: absolute;
    left: 0;
    right: 0;
    margin: 0;
    text-align: center;
    font-size: 83px;
    line-height: 1;
    font-weight: 400;
    letter-spacing: 0.085em;
    white-space: nowrap;
  }
  .tagline--first { top: 314px; color: var(--gold-text); }
  .tagline--second { top: 396px; color: var(--teal); }
  .hosts {
    position: absolute;
    left: 0;
    top: 460px;
    width: 1200px;
    height: 737px;
  }
  .footer-band {
    position: absolute;
    left: 0;
    top: 1041px;
    width: 1200px;
    height: 156px;
    background: var(--footer);
  }
  .brand-mark {
    position: absolute;
    left: 203px;
    top: 1072px;
    width: 104px;
    height: 104px;
    background: var(--teal);
  }
  .brand-name {
    position: absolute;
    left: 335px;
    top: 1066px;
    margin: 0;
    color: var(--white);
    font-family: "Montserrat", sans-serif;
    font-weight: 400;
    font-size: 53px;
    line-height: 1;
    letter-spacing: 0.035em;
    white-space: nowrap;
  }
  .brand-descriptor {
    position: absolute;
    left: 334px;
    top: 1148px;
    margin: 0;
    color: var(--white);
    font-family: "Montserrat", sans-serif;
    font-weight: 300;
    font-size: 31px;
    line-height: 1;
    letter-spacing: 0.155em;
    white-space: nowrap;
  }
</style>
</head>
<body>
  <main class="cover">
    <header class="title-block">
      <h1 class="title">LEDGER CHAT</h1>
    </header>
    <div class="format-badge">PODCAST</div>

    <p class="tagline tagline--first">STOCK PICKS, STRATEGIES</p>
    <p class="tagline tagline--second">&amp; TIPS FOR INVESTORS</p>

    <svg class="hosts" viewBox="0 0 1200 737" role="img" aria-label="Headshots of the two podcast hosts in dark suits and white shirts">
      <defs>
        <linearGradient id="hostLeft" x1="0" y1="0" x2="0" y2="1">
          <stop offset="0" stop-color="#2b211c"/>
          <stop offset="0.18" stop-color="#6e5446"/>
          <stop offset="0.45" stop-color="#c49680"/>
          <stop offset="0.7" stop-color="#8c7468"/>
          <stop offset="0.82" stop-color="#2c2f36"/>
          <stop offset="1" stop-color="#1b1d22"/>
        </linearGradient>
        <linearGradient id="hostRight" x1="0" y1="0" x2="0" y2="1">
          <stop offset="0" stop-color="#b88f78"/>
          <stop offset="0.45" stop-color="#d8a58b"/>
          <stop offset="0.7" stop-color="#b08a78"/>
          <stop offset="0.8" stop-color="#30333a"/>
          <stop offset="1" stop-color="#1d1f24"/>
        </linearGradient>
      </defs>
      <rect x="40" y="12" width="540" height="760" rx="250" fill="url(#hostLeft)"/>
      <rect x="600" y="32" width="580" height="740" rx="270" fill="url(#hostRight)"/>
    </svg>

    <footer class="footer-band"></footer>
    <div class="brand-mark"></div>
    <p class="brand-name">HALVARD FINANCIAL</p>
    <p class="brand-descriptor">INDEPENDENT EQUITY ADVISORS</p>
  </main>
</body>
</html>
```